Home Health Care Agency Needs a Website (Seeking a PSD)

We need a user friendly website for a Home Health Care Agency. Our service is for the elderly and disabled. Frequently the busy professional middle-aged married daughter will use the website to arrange in-home care for an aging parent. Therefore, our website is primarily geared towards middle-aged women. In-home care is typically 24 hours a day so, a feeling of trustworthiness and security should be effectively conveyed. (Seeking a PSD- however, if you also offer coding, please let us know the cost.)

Target Market(s)

Frequently the busy professional middle-aged married daughter (possibly out of state) will use the website to arrange in-home care for an aging parent.

Industry/Entity Type

Security

Requirements
Must have
• Website must be clean, uncluttered and professional. The following menu pages are requested: Home, About Us, Services, Resources, FAQ, Employment & Contact.
Should not have
• Must not be too whimsical.

```html
<!DOCTYPE html>
<html lang="en">
<head>
<meta charset="utf-8">
<title>Harbor Home Health</title>
<link href="https://fonts.googleapis.com/css2?family=Roboto+Condensed:ital,wght@0,400;0,700;1,700&display=swap" rel="stylesheet">
<style>
:root{
  --cream:#fbf9f1;
  --cream-dark:#efece0;
  --ink:#2b2b2b;
  --muted:#444;
  --blue:#1ab2d8;
  --blue-deep:#0a8fb4;
  --footer:#1a93ad;
  --panel-head:#e2e2e0;
  --line:#dcdad0;
  --field:#f6f5ec;
}
*{box-sizing:border-box;margin:0;padding:0}
html,body{width:1000px;height:1200px;overflow:hidden}
body{
  font-family:"Roboto Condensed",sans-serif;
  color:var(--ink);
  background:
    radial-gradient(ellipse 260px 160px at 120px 720px,rgba(220,216,200,.45),transparent 70%),
    radial-gradient(ellipse 240px 170px at 900px 760px,rgba(220,216,200,.45),transparent 70%),
    radial-gradient(ellipse 300px 120px at 500px 30px,rgba(225,222,208,.5),transparent 70%),
    var(--cream);
  position:relative;
}
.site-header{position:absolute;left:0;top:0;width:1000px;height:134px}
.brand{position:absolute;left:102px;top:34px;display:flex;align-items:center;gap:8px}
.brand-dot{width:34px;height:34px;border-radius:50%;background:var(--blue)}
.brand-name{font-size:26px;font-weight:700;color:var(--blue);line-height:1.05;width:120px}
.phone{position:absolute;left:715px;top:16px;display:flex;align-items:center;gap:8px;font-size:21px;font-weight:700;color:#555}
.main-nav{position:absolute;left:287px;top:64px;width:618px;height:58px;background:#faf9f4;border:1px solid #e6e4da;border-radius:8px;display:flex;align-items:center;padding-left:9px}
.main-nav a{font-size:14.5px;color:#222;text-decoration:none;height:38px;display:flex;align-items:center;justify-content:center;border-right:1px solid #e6e4da}
.main-nav a.active{background:var(--blue);color:#fff;border-radius:4px;border-right:none;margin-right:6px}
.main-nav a:last-child{border-right:none}
.hero{position:absolute;left:0;top:134px;width:1000px;height:454px;
  background:linear-gradient(100deg,#8b8a85 0%,#c9c3bb 25%,#e8cfc0 50%,#b6b7c7 72%,#d8d3cc 100%)}
.hero-dots{position:absolute;left:459px;top:556px;display:flex;gap:8px}
.hero-dots span{width:17px;height:17px;border-radius:50%;border:2px solid #fff;background:rgba(255,255,255,.2)}
.welcome{position:absolute;left:0;top:604px;width:1000px;text-align:center;font-size:27px;font-weight:700;color:#333}
.welcome .accent{color:var(--blue)}
.welcome i{display:inline-block;width:10px;height:10px;border-radius:50%;background:#d8d8d6;margin:0 12px;vertical-align:middle}
.welcome-rule{position:absolute;left:196px;top:640px;width:604px;height:1px;background:var(--line)}
.welcome-text{position:absolute;left:104px;top:655px;width:785px;font-size:11.6px;line-height:19.2px;text-align:justify;color:var(--muted)}
.cta{position:absolute;left:373px;top:752px;width:239px;height:32px;background:linear-gradient(#2cb8dc,#0a8cb2);border:2px solid #fff;box-shadow:0 0 0 1px #c8dfe6;border-radius:3px;color:#fff;font-size:17px;font-weight:700;display:flex;align-items:center;justify-content:center;letter-spacing:.4px}
.divider{position:absolute;left:96px;top:812px;width:807px;height:1px;background:var(--line)}
.panels{position:absolute;left:103px;top:827px;width:789px;height:263px;border:1px solid #ebe9df;border-radius:3px;background:rgba(252,251,246,.7)}
.panel{position:absolute;top:10px}
.panel + .panel{border-left:1px solid var(--line)}
.panel-head{height:29px;background:var(--panel-head);border-radius:3px;font-size:15.5px;color:#333;padding-left:12px;display:flex;align-items:center}
.panel-photo{margin-top:10px;height:97px;border-radius:3px}
.panel-text{margin-top:7px;font-size:11.2px;line-height:19.2px;text-align:justify;color:var(--muted)}
.btn{position:absolute;height:24px;background:var(--blue);color:#fff;font-size:14px;display:flex;align-items:center;justify-content:center}
.field{position:absolute;left:3px;width:232px;background:var(--field);border:1px solid #e3e1d6;border-top-color:#ccc9bd;border-left-color:#ccc9bd;font-size:11.6px;color:#333;padding:8px 9px}
.site-footer{position:absolute;left:0;top:1101px;width:1000px;height:99px;background:var(--footer);color:#fff}
.foot-brand{position:absolute;left:108px;top:20px;display:flex;align-items:center;gap:6px}
.foot-brand span:first-child{width:24px;height:24px;border-radius:50%;background:#d9e8ec}
.foot-brand span:last-child{font-size:18px;font-weight:700;color:#d9e8ec;width:90px;line-height:1.05}
.foot-nav{position:absolute;left:0;width:930px;top:35px;text-align:center;font-size:11.5px;white-space:nowrap}
.foot-nav a{color:#fff;text-decoration:none}
.foot-nav b{font-weight:400;margin:0 6px}
.copy{position:absolute;left:0;width:930px;top:57px;text-align:center;font-size:9.5px}
.connected{position:absolute;left:760px;top:12px;width:132px;text-align:right;font-size:15px;font-weight:700;font-style:italic}
.social{position:absolute;top:39px;width:82px;height:32px;border:1px solid #fff;border-radius:3px;background:#2a6fa8;font-size:9px;font-weight:700;display:flex;align-items:center;justify-content:center;gap:6px}
.social i{width:10px;height:10px;border-radius:50%;background:#fff}
</style>
</head>
<body>
<header class="site-header">
  <div class="brand"><span class="brand-dot"></span><span class="brand-name">Harbor Home Health</span></div>
  <div class="phone">
    <svg width="30" height="30" viewBox="0 0 30 30"><circle cx="15" cy="15" r="13" fill="#2aa6d6"/><circle cx="15" cy="15" r="9" fill="#5cc9ee"/><path d="M11 10c1-1 2 0 2.5 1l.6 1.3c.3.6-.3 1.2-.7 1.6.6 1.4 1.5 2.3 2.9 2.9.4-.4 1-1 1.6-.7l1.3.6c1 .5 2 1.5 1 2.5-1.5 1.5-4 .8-6.3-1.5S9.5 11.5 11 10z" fill="#fff"/></svg>
    (012) 555 014 270
  </div>
  <nav class="main-nav">
    <a class="active" href="#" style="width:67px">Home</a>
    <a href="#" style="width:100px">About Us</a>
    <a href="#" style="width:108px">Services</a>
    <a href="#" style="width:96px">Resources</a>
    <a href="#" style="width:69px">FAQ</a>
    <a href="#" style="width:107px">Employment</a>
    <a href="#" style="width:78px">Contact</a>
  </nav>
</header>

<div class="hero" role="img" aria-label="Photo of a smiling caregiver with an elderly woman"></div>
<div class="hero-dots"><span></span><span></span><span></span><span></span></div>

<h1 class="welcome"><i></i><span class="accent">Welcome</span> Message<i></i></h1>
<div class="welcome-rule"></div>
<p class="welcome-text">Lorem ipsum dolor sit amet, consectetur adipiscing elit. Phasellus quis est sit amet ipsum lacinia iaculis. Praesent et urna libero. Quisque varius lectus id fermentum varius. Integer ac rhoncus nulla. Morbi convallis vel ligula ultrices volutpat. Etiam elementum ligula in sollicitudin tincidunt. Cras feugiat velit vel tincidunt congue. Lorem ipsum dolor sit amet, consectetur adipiscing elit. Curabitur gravida elementum dui, nec consequat libero blandit in. Aenean at mauris vitae ante consectetur vehicula. Etiam congue, leo aliquet ornare pharetra, odio est blandit magna, sed pretium velit ipsum in sapien.</p>
<div class="cta">Click Here to View Details</div>
<div class="divider"></div>

<section class="panels">
  <div class="panel" style="left:11px;width:237px">
    <div class="panel-head">Services</div>
    <div class="panel-photo" role="img" aria-label="Photo of a nurse helping an elderly woman stand" style="background:linear-gradient(90deg,#8c3a32,#d8b9a4 50%,#c9c2b2)"></div>
    <p class="panel-text">Etiam elementum ligula in sollicitudin tincidunt. Cras feugiat velit vel tincidunt congue. Lorem ipsum dolor sit amet, consectetur adipiscing elit.</p>
    <div class="btn" style="left:142px;top:215px;width:93px">More Info</div>
  </div>
  <div class="panel" style="left:258px;width:257px;padding-left:12px;height:242px">
    <div class="panel-head">Resources</div>
    <div class="panel-photo" role="img" aria-label="Photo of a caregiver with an elderly man in a garden" style="margin-left:3px;background:linear-gradient(90deg,#6b8a3c,#c9c6c0 45%,#7fb548 75%,#e8ece8)"></div>
    <p class="panel-text" style="padding-left:3px">Etiam elementum ligula in sollicitudin tincidunt. Cras feugiat velit vel tincidunt congue. Lorem ipsum dolor sit amet, consectetur adipiscing elit.</p>
    <div class="btn" style="left:158px;top:215px;width:93px">More Info</div>
  </div>
  <div class="panel" style="left:525px;width:258px;padding-left:10px;height:242px">
    <div class="panel-head">Quick Message</div>
    <div class="field" style="left:13px;top:50px;height:31px">Your Name</div>
    <div class="field" style="left:13px;top:92px;height:103px">Your Message</div>
    <div class="btn" style="left:170px;top:215px;width:70px">Submit</div>
  </div>
</section>

<footer class="site-footer">
  <div class="foot-brand"><span></span><span>Harbor Home Health</span></div>
  <nav class="foot-nav"><a href="#">Home</a><b>|</b><a href="#">About Us</a><b>|</b><a href="#">Services</a><b>|</b><a href="#">Resources</a><b>|</b><a href="#">FAQ</a><b>|</b><a href="#">Employment</a><b>|</b><a href="#">Contact</a></nav>
  <div class="copy">Copyright © 2013, Harbor Home Health...</div>
  <div class="connected">Get Connected :</div>
  <div class="social" style="left:725px;background:#1f86c2"><i></i>Chatter</div>
  <div class="social" style="left:816px"><i></i>Friendline</div>
</footer>
</body>
</html>
```